依頼詳細
事務所で使用する角2、長3封筒のデザインをお願いしたいと思います。行政書士の徽章(コスモスのマーク)と、任意ですが行政書士会のマスコットキャラクター「はるとも君」なども使用できるようでしたら使用して頂ければと思います。
記載項目
東都書類代理士連合 ミントブリッジ行政書士事務所 〒167-0021 東京都世田谷区桜台5丁目12番7号K/LEAF.305 TEL03-3708-1165 FAX03-3708-1150
希望イメージ
シンプル 複雑
単色 カラフル
暗い 明るい
日常 高級
遊び心 厳粛
未来的 伝統的
女性的 男性的
希望する色
青系
納品ファイル
補足説明
依頼公開後の追記内容
先行でご提案頂いたものが、二つともはるともくんのロゴを人間入りのパターンで使用されていますが、希望としては使用するとしても猫だけワンポイント程度でお願いします。(使用しないと言う選択も当然アリです。)宜しくお願い致します。
締め切り日時を延長致しました。併せて色に関する縛りは無しに致しますので自由にご提案頂ければと思います。
■ 選んだ理由

シンプルかつ当方のイメージに近いご提案を頂きましたので選定させて頂きました。

■ 提案者全員のお礼・コメント

この度は沢山のランサーの方にご提案を頂き感謝いたします。

```html
<!DOCTYPE html>
<html lang="ja">
<head>
<meta charset="utf-8">
<title>ミントブリッジ行政書士事務所 角2封筒</title>
<link rel="stylesheet" href="https://fonts.googleapis.com/css2?family=Noto+Sans+JP:wght@400;500&display=swap">
<style>
  :root {
    --backdrop: #d9d9d9;
    --paper: #ffffff;
    --fold: #cfcfcf;
    --brand-blue: #2a5fb0;
    --ink: #555555;
    --mascot-tone: #ece6e4;
  }
  html, body {
    margin: 0;
    width: 801px;
    height: 1200px;
    overflow: hidden;
    background: var(--backdrop);
    font-family: "Noto Sans JP", sans-serif;
  }
  .envelope {
    position: absolute;
    left: 80px;
    top: 59px;
    width: 646px;
    height: 1116px;
    background: var(--paper);
  }
  .flap-line {
    position: absolute;
    left: 0;
    top: 0;
  }
  .seal-mark {
    position: absolute;
    left: 293px;
    top: 18px;
    width: 60px;
    height: 60px;
    border-radius: 50%;
    background: var(--brand-blue);
  }
  .sender {
    position: absolute;
    left: 18px;
    top: 803px;
    width: 610px;
    height: 150px;
  }
  .sender-mark {
    position: absolute;
    left: 0;
    top: 0;
    width: 66px;
    height: 66px;
    border-radius: 50%;
    background: var(--brand-blue);
  }
  .association {
    position: absolute;
    left: 83px;
    top: 6px;
    margin: 0;
    font-size: 13px;
    line-height: 18px;
    font-weight: 500;
    color: var(--brand-blue);
    letter-spacing: 0.04em;
  }
  .office-name {
    position: absolute;
    left: 81px;
    top: 26px;
    margin: 0;
    font-size: 23px;
    line-height: 32px;
    font-weight: 500;
    color: var(--brand-blue);
    white-space: nowrap;
  }
  .rule {
    position: absolute;
    left: 0;
    top: 86px;
    width: 440px;
    height: 1px;
    background: var(--brand-blue);
  }
  .mascot {
    position: absolute;
    left: 462px;
    top: -6px;
    width: 106px;
    height: 128px;
    background: linear-gradient(160deg, var(--paper), var(--mascot-tone));
    border-radius: 8px;
  }
  .contact {
    position: absolute;
    left: 0;
    top: 98px;
    margin: 0;
    font-size: 10.5px;
    line-height: 21px;
    color: var(--ink);
    font-style: normal;
    letter-spacing: 0.06em;
    white-space: nowrap;
  }
</style>
</head>
<body>
  <div class="envelope">
    <svg class="flap-line" width="646" height="120" viewBox="0 0 646 120" aria-hidden="true">
      <polyline points="0,8 24,100 622,100 646,8" fill="none" stroke="var(--fold)" stroke-width="1.2"/>
    </svg>
    <div class="seal-mark" aria-hidden="true"></div>

    <div class="sender">
      <div class="sender-mark" aria-hidden="true"></div>
      <p class="association">東都書類代理士連合</p>
      <p class="office-name">ミントブリッジ行政書士事務所</p>
      <div class="rule"></div>
      <div class="mascot" role="img" aria-label="マスコットの白い猫「はるとも君」のワンポイントイラスト"></div>
      <address class="contact">
        〒167-0021　東京都世田谷区桜台5丁目12番7号K/LEAF.305<br>
        TEL 03-5921-4472　･FAX 03-5921-4480
      </address>
    </div>
  </div>
</body>
</html>
```